Holm Tasker Dunecrest vehicle wrap

Looking for a partial wrap for our Managed IT Business.
The vehicle is a 2025 Holm Tasker Dunecrest in white.
Our main colour is orange - #f37321.
Wanting to include out website and phone number on it (below)
kestrait.com.au
1300 2 KESTRA
Please take a look at our website to how we brand.
I want to include some of our key services:
Managed IT
Cyber Security
Backup and Disaster Recovery
Looking for maybe a half or 2/3rds wrap.
I have attached my logo, and images of the vehicle.
Here is some text from our website.
Kestra IT is a forward-thinking IT partner dedicated to helping businesses across Australia stay ahead. Founded on a belief that IT should be simple, reliable, and secure, we deliver cloud solutions, cybersecurity, and managed IT services tailored to your needs.
Based in Goulburn, we work with small to medium businesses across industries like trades, professional services, and regional enterprises — simplifying technology so you can focus on what matters most.
At Kestra IT, we pride ourselves on being easy to work with, highly responsive, and committed to real results. We don’t just fix problems — we help prevent them, giving you peace of mind that your IT is in expert hands. Whether you need day-to-day support or a full IT strategy, Kestra IT is here to keep your business moving forward.
Every solution we deliver is backed by honest advice, genuine care, and a deep understanding of what it takes to keep businesses running smoothly.

```html
<!DOCTYPE html>
<html lang="en">
<head>
<meta charset="utf-8">
<title>Kestra IT – Vehicle Wrap Side Panel</title>
<link rel="stylesheet" href="https://fonts.googleapis.com/css2?family=Poppins:wght@400;600;700;800&display=swap">
<style>
  :root {
    --brand-orange: #e2691f;
    --brand-black: #0d0d0d;
    --paper: #ffffff;
    --text-light: #ffffff;
  }
  * { margin: 0; padding: 0; box-sizing: border-box; }
  html, body {
    width: 1200px;
    height: 675px;
    overflow: hidden;
    background: var(--paper);
    font-family: "Poppins", sans-serif;
  }
  .canvas {
    position: relative;
    width: 1200px;
    height: 675px;
    overflow: hidden;
    background: var(--paper);
  }
  .wrap-graphics {
    position: absolute;
    inset: 0;
  }
  .brand-name {
    position: absolute;
    left: 150px;
    top: 282px;
    font-size: 86px;
    font-weight: 800;
    letter-spacing: -2px;
    line-height: 1;
    color: var(--brand-black);
    transform: rotate(-3deg);
    transform-origin: left center;
  }
  .service-list {
    position: absolute;
    left: 560px;
    top: 262px;
    list-style: none;
    color: var(--text-light);
    font-size: 18px;
    font-weight: 700;
    line-height: 1.3;
    transform: rotate(-4deg);
    transform-origin: left top;
  }
  .service-list li::before {
    content: "• ";
    font-size: 14px;
  }
  .service-list .indent { padding-left: 12px; }
  .service-list .indent::before { content: ""; }
  .phone {
    position: absolute;
    left: 744px;
    top: 252px;
    display: flex;
    align-items: center;
    gap: 12px;
    transform: rotate(-3deg);
    transform-origin: left center;
  }
  .phone-icon { width: 44px; height: 44px; flex: none; }
  .phone-number {
    font-size: 40px;
    font-weight: 700;
    color: var(--brand-black);
    letter-spacing: -0.5px;
    line-height: 1;
    white-space: nowrap;
  }
  .social-dots {
    position: absolute;
    left: 1030px;
    top: 334px;
    display: flex;
    gap: 8px;
  }
  .social-dot {
    width: 26px;
    height: 26px;
    border-radius: 50%;
    background: var(--brand-orange);
  }
  .website {
    position: absolute;
    left: 510px;
    top: 395px;
    font-size: 32px;
    font-weight: 400;
    color: var(--text-light);
    transform: rotate(-5deg);
    transform-origin: left center;
    white-space: nowrap;
  }
  .website strong { font-weight: 700; }
</style>
</head>
<body>
<main class="canvas">
  <svg class="wrap-graphics" viewBox="0 0 1200 675" width="1200" height="675" aria-hidden="true">
    <polygon class="panel-orange" points="60,240 1140,200 1140,470 60,470" fill="var(--brand-orange)"/>
    <polygon class="stripe-top" points="60,240 1140,200 1140,222 60,264" fill="var(--brand-black)"/>
    <polygon class="banner-web" points="460,420 900,362 930,338 1140,306 1140,372 470,468 520,440" fill="var(--brand-black)"/>
  </svg>

  <div class="brand-name">kestra it</div>

  <ul class="service-list">
    <li>Managed IT</li>
    <li>Cyber Security</li>
    <li>Backup &amp; Disaster</li>
    <li class="indent">Recovery</li>
  </ul>

  <div class="phone">
    <svg class="phone-icon" viewBox="0 0 48 48" aria-hidden="true">
      <circle cx="24" cy="24" r="21" fill="none" stroke="#fff" stroke-width="3.5"/>
      <path d="M17 13c1.5-1 3-.5 3.6.8l1.8 3.8c.5 1.1.2 2.3-.7 3l-1.6 1.2c1 2.6 3 4.7 5.6 5.9l1.2-1.6c.7-.9 2-1.2 3-.7l3.8 1.8c1.3.6 1.8 2.2.8 3.6l-1.6 2.3c-.9 1.2-2.4 1.7-3.8 1.2C21.8 31.6 16.2 26 13.6 18.8c-.5-1.4 0-2.9 1.2-3.8z" fill="#fff"/>
    </svg>
    <span class="phone-number">1300 2 KESTRA</span>
  </div>

  <div class="social-dots" aria-label="Social channels">
    <span class="social-dot"></span>
    <span class="social-dot"></span>
  </div>

  <div class="website">www.<strong>kestrait</strong>.com.au</div>
</main>
</body>
</html>
```